What's wrong with sitting graphic for ProLattice

Design an info-graphic for posting to ProLattice (correct size for ProLattice) - which explains the health issues with sitting at work. Based on the attached powerpoint mock up. <br/>This can use the image 317264905 from Framevault which I can buy and send to the designer. Or designer can create own image of person sitting at a desk.

```html
<!DOCTYPE html>
<html lang="en">
<head>
<meta charset="utf-8">
<title>What are the health risks of sitting?</title>
<link rel="stylesheet" href="https://fonts.googleapis.com/css2?family=Montserrat:wght@700;800&family=Roboto:wght@400&family=Roboto+Condensed:wght@400;700&display=swap">
<style>
  :root {
    --navy-deep: #08395a;
    --navy: #0d4d74;
    --navy-light: #15638f;
    --wave: rgba(255,255,255,0.05);
    --line: #d9e6ee;
    --white: #ffffff;
    --label: #eef4f8;
    --icon: #2a3440;
    --panel: rgba(150,190,214,0.45);
    --figure-a: #2f6d92;
    --figure-b: #1d587c;
  }
  * { margin: 0; padding: 0; box-sizing: border-box; }
  html, body { width: 1200px; height: 954px; overflow: hidden; background: var(--navy-deep); }
  .canvas {
    position: relative; width: 1200px; height: 954px; overflow: hidden;
    background: linear-gradient(160deg, var(--navy-light) 0%, var(--navy) 45%, var(--navy-deep) 100%);
    font-family: "Roboto", sans-serif; color: var(--white);
  }
  .waves { position: absolute; inset: 0; }
  .brand {
    position: absolute; top: 46px; left: 0; width: 100%; text-align: center;
    font-family: "Montserrat", sans-serif; font-weight: 800; font-size: 30px;
    letter-spacing: -0.5px; color: var(--white);
  }
  .title {
    position: absolute; top: 120px; left: 0; width: 100%; text-align: center;
    font-family: "Montserrat", sans-serif; font-weight: 700; font-size: 45px; color: var(--white);
  }
  .timeline { position: absolute; inset: 0; }
  .risk-label {
    position: absolute; font-size: 25px; line-height: 33px; color: var(--label);
  }
  .risk-label.side { text-align: right; width: 160px; }
  .risk-label.below { text-align: center; width: 200px; }
  .scene {
    position: absolute; left: 292px; top: 298px; width: 572px; height: 410px;
    background: radial-gradient(ellipse at 45% 55%, var(--figure-a) 0%, var(--figure-b) 55%, transparent 78%);
    border-radius: 40px;
  }
  .answer-panel {
    position: absolute; left: 881px; top: 232px; width: 277px; height: 420px;
    background: var(--panel); text-align: center;
    font-family: "Roboto Condensed", sans-serif; color: var(--white);
  }
  .answer-panel h2 { margin-top: 62px; font-weight: 700; font-size: 29px; }
  .answer-panel p { margin-top: 40px; font-size: 25px; line-height: 36px; }
</style>
</head>
<body>
<div class="canvas">
  <svg class="waves" width="1200" height="954" viewBox="0 0 1200 954" aria-hidden="true">
    <path d="M700 0 C820 120 1000 60 1200 150 L1200 0 Z" fill="var(--wave)"/>
    <path d="M0 560 C260 520 480 640 760 600 C960 570 1080 640 1200 620 L1200 954 L0 954 Z" fill="var(--wave)"/>
    <path d="M520 954 C700 820 940 880 1200 760 L1200 954 Z" fill="var(--wave)"/>
  </svg>

  <div class="brand">corvanta</div>
  <h1 class="title">What are the health risks of sitting?</h1>

  <svg class="timeline" width="1200" height="954" viewBox="0 0 1200 954" aria-hidden="true">
    <g stroke="var(--line)" stroke-width="2" fill="none">
      <path d="M225 273 V777 H905"/>
    </g>
    <g fill="var(--white)" stroke="var(--line)" stroke-width="2">
      <circle cx="225" cy="273" r="33"/>
      <circle cx="225" cy="466" r="33"/>
      <circle cx="225" cy="655" r="33"/>
      <circle cx="330" cy="777" r="33"/>
      <circle cx="522" cy="777" r="33"/>
      <circle cx="690" cy="777" r="33"/>
      <circle cx="904" cy="777" r="33"/>
    </g>
    <g fill="none" stroke="var(--icon)" stroke-width="2" stroke-linecap="round" stroke-linejoin="round">
      <!-- cell -->
      <circle cx="225" cy="273" r="12"/>
      <circle cx="225" cy="273" r="4"/>
      <path d="M225 255v-4M225 291v4M207 273h-4M243 273h4M212 260l-3-3M238 286l3 3M238 260l3-3M212 286l-3 3"/>
      <!-- brain -->
      <path d="M225 452c-8-6-20 0-18 10-6 4-4 14 2 16 2 8 12 10 16 4 4 6 14 4 16-4 6-2 8-12 2-16 2-10-10-16-18-10z"/>
      <path d="M225 452v30"/>
      <!-- heart -->
      <path d="M225 670c-14-10-20-18-16-26 4-7 12-6 16 0 4-6 12-7 16 0 4 8-2 16-16 26z"/>
      <!-- glucose meter -->
      <rect x="314" y="766" width="26" height="18" rx="4"/>
      <path d="M319 772h14M319 778h8"/>
      <path d="M346 784c0-4 4-8 4-8s4 4 4 8a4 4 0 0 1-8 0z" stroke="#b0254a"/>
      <!-- figure -->
      <circle cx="522" cy="762" r="6"/>
      <path d="M510 792c-2-12 2-22 12-22s14 10 12 22z"/>
      <!-- pulse -->
      <path d="M672 777h8l4-10 6 20 5-14 3 4h10" stroke="#c8243a"/>
      <!-- spine -->
      <path d="M898 758h12M896 768h14M896 778h14M897 788h12M899 798h8"/>
      <path d="M888 770l-6-4M920 784l6 4" stroke="#2c7fd0"/>
    </g>
  </svg>

  <div class="risk-label side" style="left:10px; top:256px;">Cancer</div>
  <div class="risk-label side" style="left:10px; top:449px;">Strokes</div>
  <div class="risk-label side" style="left:10px; top:637px;">Heart<br>attack</div>
  <div class="risk-label below" style="left:230px; top:830px;">Type 2<br>diabetes</div>
  <div class="risk-label below" style="left:422px; top:834px;">Metabolic<br>syndrome</div>
  <div class="risk-label below" style="left:590px; top:830px;">Premature<br>Death</div>
  <div class="risk-label below" style="left:804px; top:830px;">Musculoskeletal<br>pain</div>

  <div class="scene" role="img" aria-label="Illustration of an office worker seen from behind, sitting on an office chair at a white desk with a monitor showing a bar chart and stacks of papers"></div>

  <div class="answer-panel">
    <h2>The answer?</h2>
    <p>GET MOVING<br>With a<br>standing desk<br>&amp; sit stand<br>coaching<br>software.</p>
  </div>
</div>
</body>
</html>
```